B2B EDM Banner Design- Specialist Tech Company

We need a new top-of-email banner for our EDM campaigns for Varnel Brix (www.varnelbrix-example.com
). This banner will sit at the top of every email and must immediately signal the brand, look modern and professional, and be visually aligned with the tech/IT audience.
Size of the banner: Around 728x90 - it must fit at the top of an email blast.
Purpose of the Banner
Establish a strong, recognizable brand identity across all Varnel Brix EDMs
visually consistent with existing banners created for other brands (see reference examples provided)
Communicate Varnel Brix’s value proposition at a glance
Brand Name
Varnel Brix
Tagline (must appear in the banner)
“11,322 whitepapers from 726 companies”
Design Requirements
Style & Tone
Modern, clean, and professional
Tech-centric look and feel
High-quality, sleek, and corporate
Eye-catching but not cluttered
Should feel premium and authoritative
Layout & Composition
Full-width banner for email header
Horizontal orientation similar to the Plomtar and Quindle Staff Archive examples
Include space for the brand name/logo prominently on the left or centered
Integrate the tagline in a readable, secondary position
Optional: a subtle background texture or tech-related abstract pattern (circuitry, network nodes, gradient, etc.)
No busy imagery—should feel clean and trustworthy
Color Palette
Use colors consistent with Varnel Brix branding from www.varnelbrix-example.com
Blues, greys, blacks, and tech-style gradients preferred
Should feel consistent with a B2B IT audience
Typography
Clean, sans-serif fonts (professional/tech-aligned)
Brand name should be bold and prominent
Tagline should be smaller, but still readable on desktop and mobile
Imagery (if used)
Abstract tech shapes, network visuals, geometric patterns, or gradient overlays
Avoid photography of people
Keep imagery subtle so text remains legible
Call-to-Action Button (optional)
None required in this banner (unlike the HR examples)
Banner should remain a pure brand header
Deliverables
Final banner in PNG and JPG formats
2–3 design variations (if possible) for A/B testing
Dimensions optimized for EDM: ~600–700px wide (standard email width), proportionate height

```html
<!DOCTYPE html>
<html lang="en">
<head>
<meta charset="utf-8">
<title>Varnel Brix – Email Header Banner</title>
<link rel="stylesheet" href="https://fonts.googleapis.com/css2?family=Poppins:wght@400;500;600;700&display=swap">
<style>
  :root {
    --page-bg: #ffffff;
    --navy-deep: #040b3d;
    --navy-mid: #0a1b6b;
    --navy-glow: #1b3fa8;
    --accent-blue: #4fb6ff;
    --accent-cyan: #3fd0ff;
    --text-white: #ffffff;
    --text-soft: #d8e6ff;
    --globe-core: #3a8dff;
    --globe-edge: #0b2a8a;
  }

  * { margin: 0; padding: 0; box-sizing: border-box; }

  html, body {
    width: 1200px;
    height: 262px;
    overflow: hidden;
    background: var(--page-bg);
  }

  .canvas {
    position: relative;
    width: 1200px;
    height: 262px;
  }

  .banner {
    position: absolute;
    left: 58px;
    top: 64px;
    width: 1086px;
    height: 134px;
    overflow: hidden;
    background:
      radial-gradient(ellipse 420px 160px at 150px 140px, rgba(40, 110, 230, 0.45), transparent 70%),
      linear-gradient(90deg, var(--navy-mid) 0%, var(--navy-deep) 55%, #061050 80%, var(--navy-mid) 100%);
    box-shadow: 0 14px 18px rgba(0, 0, 0, 0.35);
    font-family: "Poppins", sans-serif;
  }

  .circuit-glow {
    position: absolute;
    left: 0;
    bottom: 0;
    width: 520px;
    height: 40px;
    background: linear-gradient(90deg, rgba(63, 208, 255, 0.18), rgba(63, 208, 255, 0.05) 70%, transparent);
  }

  .globe-visual {
    position: absolute;
    right: 0;
    top: 0;
    width: 180px;
    height: 134px;
    background:
      radial-gradient(circle at 110px 62px, var(--globe-core) 0%, #1d5fe0 30%, var(--globe-edge) 60%, transparent 80%);
  }

  .brand {
    position: absolute;
    left: 52px;
    top: 38px;
    display: flex;
    align-items: center;
    gap: 22px;
  }

  .brand-mark {
    width: 50px;
    height: 50px;
    border-radius: 50%;
    background: var(--accent-blue);
    flex-shrink: 0;
  }

  .brand-text {
    display: flex;
    flex-direction: column;
    width: 238px;
  }

  .brand-name {
    color: var(--text-white);
    font-weight: 700;
    font-size: 31px;
    line-height: 1;
    letter-spacing: 0.3px;
    text-transform: uppercase;
    white-space: nowrap;
  }

  .brand-rule {
    height: 1px;
    margin: 8px 0 7px;
    background: var(--accent-blue);
  }

  .brand-tagline {
    color: var(--text-soft);
    font-weight: 500;
    font-size: 11px;
    letter-spacing: 3.3px;
    text-transform: uppercase;
    white-space: nowrap;
  }

  .value-line {
    position: absolute;
    left: 420px;
    top: 55px;
    color: var(--text-white);
    font-weight: 500;
    font-size: 22px;
    line-height: 1.1;
    white-space: nowrap;
  }

  .value-line .figure {
    color: var(--accent-blue);
  }
</style>
</head>
<body>
  <div class="canvas">
    <header class="banner">
      <div class="circuit-glow" role="img" aria-label="Faint glowing circuit-board lines"></div>
      <div class="globe-visual" role="img" aria-label="Glowing blue digital globe with network connections"></div>

      <div class="brand">
        <span class="brand-mark"></span>
        <div class="brand-text">
          <span class="brand-name">Varnel Brix</span>
          <span class="brand-rule"></span>
          <span class="brand-tagline">For Tech Professionals</span>
        </div>
      </div>

      <p class="value-line"><span class="figure">11,322</span> whitepapers from <span class="figure">726</span> companies</p>
    </header>
  </div>
</body>
</html>
```